I need a new business card design for my pharmacy.

I need a business card design. I will include my logo.
The card needs to be readable. I prefer to have my logo on one side along with my website, the other side includes the other information. Please use combination of black, neon green, white, and silver. This needs to catch the eye but yet be clearly visible and legible. Thanks

Industry/Entity Type

Pharmacy

Contact Information for Business Card

It needs to have the following information listed:
Mel's Apothecary Owner/Pharm D.
7134 North Brook Lane
Sioux Falls, SD 57231
Phone 605-318-6207
Fax 605-318-6209
email: mel@melsapothecary-example.com
www.melsapothecary-example.com
Store hours Monday-Friday 8 am- 7 pm
Saturday 8 am- 12 pm
Sunday Closed
Please utilize the colors black, white, and neon green, maybe silver.

Requirements
Must have
• It needs to be easily readable!
Nice to have
• It should catch the eye.
Should not have
• Do not use any other colors except listed: black, neon green, white, & silver.

```html
<!DOCTYPE html>
<html lang="en">
<head>
<meta charset="utf-8">
<title>Mel's Apothecary – Business Card</title>
<link rel="stylesheet" href="https://fonts.googleapis.com/css2?family=Quicksand:wght@400;500;600&family=Varela+Round&display=swap">
<style>
  :root {
    --backdrop: #2b2b2c;
    --ink: #464648;
    --ink-soft: #6a6a6c;
    --silver: #9a9a9c;
    --paper: #ffffff;
    --lime: #b9d35a;
    --lime-light: #c3da68;
    --lime-deep: #aecb4c;
  }
  * { box-sizing: border-box; margin: 0; padding: 0; }
  html, body {
    width: 1200px; height: 799px; overflow: hidden;
    background: var(--backdrop);
  }
  .canvas { position: relative; width: 1200px; height: 799px; }

  .card { position: absolute; overflow: hidden; background: var(--paper); }

  /* ---------- Back: hours + contact ---------- */
  .card-back { left: 120px; top: 100px; width: 340px; height: 598px; }

  .hours { position: absolute; left: 0; top: 0; width: 100%; height: 268px; padding: 22px 22px 0 22px; }
  .hours-title {
    font-family: "Varela Round", sans-serif;
    font-size: 40px; color: var(--ink); letter-spacing: 0.5px; line-height: 1;
  }
  .hours-table { position: relative; margin-top: 18px; height: 190px; }
  .day-list { list-style: none; font-family: "Quicksand", sans-serif; font-size: 17px; color: var(--ink); }
  .day-list li { height: 26px; line-height: 26px; padding-left: 16px; position: relative; }
  .day-list li::before {
    content: ""; position: absolute; left: 2px; top: 10px; width: 7px; height: 7px; background: var(--lime);
  }
  .day-list li.day-closed::before { background: var(--ink); }
  .hours-rule { position: absolute; left: 152px; width: 1px; background: var(--silver); }
  .hours-rule.weekdays { top: 6px; height: 118px; }
  .hours-rule.weekend { top: 136px; height: 44px; }
  .hours-time {
    position: absolute; left: 168px;
    font-family: "Quicksand", sans-serif; font-size: 19px; color: var(--ink);
  }
  .hours-time.weekdays { top: 52px; }
  .hours-time.saturday { top: 132px; }
  .hours-time.sunday { top: 158px; left: 186px; }

  .contact { position: absolute; left: 0; top: 268px; width: 100%; height: 200px; background: var(--lime-light); padding: 18px 22px 0 22px; }
  .owner-name { font-family: "Varela Round", sans-serif; font-size: 24px; color: var(--ink); line-height: 1.1; }
  .owner-role { font-family: "Quicksand", sans-serif; font-weight: 600; font-size: 15px; color: var(--ink); margin-top: 2px; }
  .owner-badge { position: absolute; right: 24px; top: 24px; width: 42px; height: 42px; border-radius: 50%; background: var(--paper); }
  .contact-rule { position: absolute; left: 22px; top: 84px; width: 220px; height: 2px; background: var(--paper); }
  .contact-list { list-style: none; position: absolute; left: 22px; top: 96px; font-family: "Quicksand", sans-serif; font-weight: 500; font-size: 15px; color: var(--ink); }
  .contact-list li { display: flex; align-items: flex-start; gap: 8px; line-height: 19px; margin-bottom: 2px; }
  .contact-list svg { flex: none; width: 18px; height: 18px; margin-top: 1px; }

  .signoff { position: absolute; left: 0; top: 468px; width: 100%; height: 130px; background: var(--lime-deep); border-top: 2px solid var(--paper); }
  .signoff-inner { position: absolute; left: 22px; right: 22px; top: 30px; height: 60px; display: flex; align-items: center; gap: 16px; }
  .signoff-dot { width: 30px; height: 30px; border-radius: 50%; background: var(--paper); flex: none; }
  .signoff-divider { width: 1px; height: 54px; background: var(--paper); }
  .signoff-name { font-family: "Varela Round", sans-serif; font-size: 24px; color: var(--ink); }
  .signoff-rule { position: absolute; left: 22px; right: 22px; bottom: 18px; height: 2px; background: var(--paper); }

  /* ---------- Front: name + website ---------- */
  .card-front { left: 520px; top: 229px; width: 598px; height: 340px; }
  .front-band { position: absolute; left: 0; top: 0; width: 226px; height: 100%; background: var(--lime); }
  .front-mark { position: absolute; left: 420px; top: 46px; width: 120px; height: 120px; border-radius: 50%; border: 14px solid var(--ink); }
  .front-name {
    position: absolute; left: 244px; top: 196px;
    font-family: "Varela Round", sans-serif; font-size: 40px; color: var(--ink); line-height: 1; white-space: nowrap;
  }
  .front-web {
    position: absolute; left: 246px; top: 252px;
    font-family: "Quicksand", sans-serif; font-weight: 500; font-size: 21px; color: var(--lime); white-space: nowrap;
  }
</style>
</head>
<body>
<main class="canvas">

  <section class="card card-back" aria-label="Business card back">
    <div class="hours">
      <h2 class="hours-title">Store hours</h2>
      <div class="hours-table">
        <ul class="day-list">
          <li>Monday</li>
          <li>Tuesday</li>
          <li>Wednesday</li>
          <li>Thursday</li>
          <li>Friday</li>
          <li>Saturday</li>
          <li class="day-closed">Sunday</li>
        </ul>
        <span class="hours-rule weekdays"></span>
        <span class="hours-rule weekend"></span>
        <span class="hours-time weekdays">8 am - 7 pm</span>
        <span class="hours-time saturday">8 am - 12 pm</span>
        <span class="hours-time sunday">CLOSED</span>
      </div>
    </div>

    <div class="contact">
      <h1 class="owner-name">Mel's Apothecary</h1>
      <p class="owner-role">Owner/Pharm D</p>
      <span class="owner-badge"></span>
      <span class="contact-rule"></span>
      <ul class="contact-list">
        <li>
          <svg viewBox="0 0 18 18" aria-label="Address"><rect x="1" y="4" width="16" height="11" fill="#fff"/><path d="M1 4 L9 10 L17 4" fill="none" stroke="#b9d35a" stroke-width="1.5"/></svg>
          <span>7134 North Brook Lane<br>Sioux Falls, SD 57231</span>
        </li>
        <li>
          <svg viewBox="0 0 18 18" aria-label="Phone"><path d="M4 2 L7 2 L8 6 L6 7.5 C7 10 8.5 11.5 10.5 12.5 L12 10.5 L16 11.5 L16 14.5 C16 15.5 15 16 14 16 C8 15.5 2.5 10 2 4 C2 3 3 2 4 2 Z" fill="#fff"/></svg>
          <span>605-318-6207</span>
        </li>
        <li>
          <svg viewBox="0 0 18 18" aria-label="Fax"><rect x="5" y="1.5" width="8" height="5" fill="#fff"/><rect x="2" y="7" width="14" height="7" rx="1" fill="#fff"/><rect x="5" y="12" width="8" height="4.5" fill="#fff" stroke="#c3da68" stroke-width="1"/></svg>
          <span>605-318-6209</span>
        </li>
        <li>
          <svg viewBox="0 0 18 18" aria-label="Email"><circle cx="9" cy="9" r="7.5" fill="none" stroke="#fff" stroke-width="2"/><circle cx="9" cy="9" r="3" fill="none" stroke="#fff" stroke-width="2"/></svg>
          <span>mel@melsapothecary-example.com</span>
        </li>
      </ul>
    </div>

    <div class="signoff">
      <div class="signoff-inner">
        <span class="signoff-dot"></span>
        <span class="signoff-divider"></span>
        <span class="signoff-name">Mel's Apothecary</span>
      </div>
      <span class="signoff-rule"></span>
    </div>
  </section>

  <section class="card card-front" aria-label="Business card front">
    <div class="front-band"></div>
    <span class="front-mark"></span>
    <p class="front-name">Mel's Apothecary</p>
    <p class="front-web">melsapothecary-example.com</p>
  </section>

</main>
</body>
</html>
```